Indie Filmmakers Need Awesome Documentary Poster

BRAVEL Productions, an independent film/video production company needs a poster to publicize its upcoming documentary entitled, "Harbor Of Dust". Harbor Of Dust is a film about the underground world of guerilla film collectors and preservationists. These people are not usually associated with an archive nor do they really make any money off their work. They collect, share and preserve films using money from their "day jobs" to save them for future generations. They are fighting the goliaths of unfair copyright laws and studio negligence in order to preserve what is often the last print of an old film for future generations. One of our subjects actually dumpster dives for film and restores it. Another actually won a special gilden prize for his work during the making of our film.

We are looking for one of two poster designs (we can't decide which to go with yet).
But first, a bit about the overall feel and look we are hoping for. Because these subjects are really heroes to us, we would like the tone of the poster to reflect that so we're not going for laughs here at all.

Design 1 (We call it the Pizza Design) is based on the visual of the last piece of pizza on an otherwise empty cardboard circle except instead of a slice of pizza, it should be a section of a film reel (cut in the classic triangle pizza shape). Title "Harbor Of Dust" must be prominently featured as well as the tagline "Hurry! They're saving you a piece!"

Design 2 (We call it Dumpster Victory Design) is set up as follows: In the foreground is a dumpster with a figure standing triumphantly in it. The figure’s hand is raised above his head in a pose of victory clutching a film reel from which strips of film cascade down around his shoulders. We are including a picture of the face we'd like on that figure. He has wild hair and quite a beard. The dumpster can be filled with unspooled film as well. We are including a screencap of a statue that gives an idea of the way we’d like the film reel and strips to cascade around the figure. In the background, we’d like see a studio soundstage door or gates to a studio implying our guy is outside the studio diving in their dumpster. The dumpster could even have “studio trash” stenciled on it. Peeking out of the dumpster could also be iconic items like the sled from Marrow Tidewell, Baltasar’s hat, and again, the title “Harbor Of Dust” should figure prominently in the design as well as the tagline “Stopping at nothing to save your film history!”

Design 3 (Your design) Is whatever you as an artist thinks will best communicate the sense of urgency, subject matter (guerilla film preservation and collectors as the heroic keepers of lost film, etc.)

Please note the tagline changes depending on which design you are creating.

We are attaching some photos that you could use to help visualize the design.

Specs:
• Title should be predominantly featured: “Harbor Of Dust”
• Above title should read: “BRAVEL Productions Presents:”
• Tagline should be included (see above as tagline differs depending on design)
• Final product should be 27 x 40 inches (portrait style)
• File should be in editable layered photoshop file, 300 dpi
• Editable credit block should be at bottom of poster, please include (as part of credit block) Written, Produced, Directed and Edited by Miriam L. Okafor & Dov R. Hemming
• Under credit block predominant text should read: www.harborofdustpix.net

Target Market(s)

Movie goers, distribution executives at studios, film festival attendees. This needs to look like a poster you would find in an American movie house. Thanks!

Industry/Entity Type

Hair

Font styles to use
Sans Serif

Requirements
Must have
• Must haves are listed in project description above.
Nice to have
• More of the design #2 concepts of the guy in the dumpster triumphantly holding the film reel above his head in victory.
Should not have
• NOTE: We've been getting a lot of flat kind of movie reel ideas. We need it to appear more three dimensional like a pizza in a pizza box with the ghost of the reel on the cardboard and a hand picking up the last slice of the reel (maybe with some film strips hanging from the reel and some snippets in the box like it's the last piece of pizza.) We are attaching a mockup picture for your inspiration (see file called "Pizza Idea Mockup" below please). Do not use this photo for the poster. Thanks so much (and please, we are hoping someone is working on the dumpster idea too).

```html
<!DOCTYPE html>
<html lang="en">
<head>
<meta charset="utf-8">
<title>Harbor Of Dust — Poster</title>
<link rel="stylesheet" href="https://fonts.googleapis.com/css2?family=Oswald:wght@400;500&family=Stardos+Stencil:wght@700&display=swap">
<style>
  :root {
    --backdrop: #d9d9d7;
    --paper-light: #ececec;
    --paper-dark: #d6d6d6;
    --ink: #565656;
    --ink-soft: #6a6a6a;
    --reel-light: #c9c9c7;
    --reel-dark: #6f6f6d;
  }
  * { margin: 0; padding: 0; box-sizing: border-box; }
  html, body {
    width: 1200px;
    height: 1148px;
    overflow: hidden;
    background: var(--backdrop);
  }
  .poster {
    position: absolute;
    left: 232px;
    top: 9px;
    width: 736px;
    height: 1130px;
    overflow: hidden;
    background: radial-gradient(ellipse at 50% 30%, var(--paper-light) 0%, var(--paper-dark) 100%);
    color: var(--ink);
  }
  .poster__artwork {
    position: absolute;
    left: 250px;
    top: 112px;
    width: 300px;
    height: 260px;
  }
  .poster__tagline {
    position: absolute;
    left: 0;
    top: 400px;
    width: 100%;
    text-align: center;
    font-family: "Oswald", sans-serif;
    font-weight: 400;
    font-size: 17px;
    letter-spacing: 2px;
    text-transform: uppercase;
    color: var(--ink-soft);
  }
  .poster__presenter {
    position: absolute;
    left: 97px;
    top: 484px;
    font-family: "Oswald", sans-serif;
    font-weight: 500;
    font-size: 16px;
    letter-spacing: 1.2px;
    text-transform: uppercase;
    color: var(--ink);
  }
  .poster__title {
    position: absolute;
    left: 93px;
    top: 512px;
    font-family: "Stardos Stencil", sans-serif;
    font-weight: 700;
    font-size: 112px;
    line-height: 100px;
    letter-spacing: 1px;
    text-transform: uppercase;
    color: var(--ink);
  }
  .poster__title span { display: block; }
  .credits {
    position: absolute;
    left: 97px;
    top: 850px;
    width: 560px;
    font-family: "Oswald", sans-serif;
    text-transform: uppercase;
    color: var(--ink);
  }
  .credits__row {
    display: flex;
    align-items: center;
    gap: 4px;
    height: 22px;
    white-space: nowrap;
  }
  .credits__name {
    font-size: 12.5px;
    font-weight: 500;
  }
  .credits__role {
    display: inline-block;
    font-size: 5.5px;
    line-height: 6px;
    font-weight: 400;
    color: var(--ink-soft);
    text-align: right;
  }
  .poster__website {
    position: absolute;
    left: 97px;
    top: 980px;
    font-family: "Oswald", sans-serif;
    font-weight: 500;
    font-size: 24px;
    letter-spacing: 1.5px;
    color: var(--ink);
  }
</style>
</head>
<body>
  <main class="poster">
    <svg class="poster__artwork" viewBox="0 0 300 260" role="img" aria-label="Photograph of a vintage metal film reel beside its labelled film can, with a strip of film unspooling">
      <defs>
        <radialGradient id="reelTone" cx="50%" cy="45%" r="55%">
          <stop offset="0%" stop-color="var(--reel-light)"/>
          <stop offset="100%" stop-color="var(--reel-dark)"/>
        </radialGradient>
      </defs>
      <ellipse cx="150" cy="120" rx="148" ry="110" fill="url(#reelTone)"/>
    </svg>

    <p class="poster__tagline">Hurry! They're saving you a piece!</p>

    <p class="poster__presenter">Bravel Productions Presents</p>

    <h1 class="poster__title">
      <span>Harbor</span>
      <span>Of</span>
      <span>Dust</span>
    </h1>

    <section class="credits">
      <div class="credits__row">
        <span class="credits__name">Studio Name Pictures</span>
        <span class="credits__role">presents<br>a</span>
        <span class="credits__name">Producers</span>
        <span class="credits__role">a film<br>by</span>
        <span class="credits__name">Script Writer Actor Two "Movie Title"</span>
      </div>
      <div class="credits__row">
        <span class="credits__role">music<br>by</span>
        <span class="credits__name">The Musian</span>
        <span class="credits__role">costume<br>designer</span>
        <span class="credits__name">Designer Name</span>
        <span class="credits__role">edited<br>by</span>
        <span class="credits__name">Editors Name</span>
        <span class="credits__role">production<br>designer</span>
        <span class="credits__name">Designers Name</span>
        <span class="credits__role">director of<br>photography</span>
        <span class="credits__name">Cinematographer</span>
      </div>
      <div class="credits__row">
        <span class="credits__role">executive<br>producer</span>
        <span class="credits__name">Ex Producer 1 Ex Producer 2</span>
        <span class="credits__role">produced<br>by</span>
        <span class="credits__name">Producer One Producer 2</span>
        <span class="credits__role">story<br>by</span>
        <span class="credits__name">Story Writer</span>
      </div>
      <div class="credits__row">
        <span class="credits__role">screenplay<br>by</span>
        <span class="credits__name">Screen Writer</span>
        <span class="credits__role">directed<br>by</span>
        <span class="credits__name">Director Name</span>
      </div>
      <div class="credits__row">
        <span class="credits__role">written, produced,<br>directed &amp; edited by</span>
        <span class="credits__name">Miriam L. Okafor &amp; Dov R. Hemming</span>
      </div>
    </section>

    <p class="poster__website">www.harborofdustpix.net</p>
  </main>
</body>
</html>
```